Business card design/logo/website name

I am a business coach. My business name is DKA (Dunmore Kesby & Associates, Inc.) I want to use this card just for coaching. I do two kinds: Personal Image coach and Executive business coach
1. I work with people to become a polished global professional.
"Become a confident, savvy professional building relationships tactfully and appropriately while clearly representing your own company’s message and image.
Learn the nuances… Master the skills… Use the business etiquette techniques and protocols that allow you to seamlessly and confidently conduct business in a global business environment.
Have the comfort of knowing what to expect, what to do and how to easily build long and short-term relationships that give you the winning edge and increased company profits."
2. Leadership Coaching
For increasing the team’s productivity by building stronger relationships. Build strong compelling vision and write and share their Personal Leadership Philosophy, a roadmap that is concise and commanding and gives the team a clear vision of the leader's expectations.

DKA should be the logo. (Downplay the Dunmore Kesby and Associates, Inc.)

Want:
Executive Coach
Consultant

Reason: I am traveling and connections are often broken.

Target Market(s)

Executives, business people

Industry/Entity Type

Building

Font styles to use
Sans Serif
Script

Colors
0255a3
3176b5
85acd3
ec2027

Requirements
Must have
• DKA as the logo,(no preference on how you treat DKA) with Dunmore Kesby & Associates. Inc. downplayed.
On the card:
Rosalind Kesby CEO
Executive Coach
Consultant
NVQ 4(c)
Coaching - Training - Strategic Planning

```html
<!DOCTYPE html>
<html lang="en">
<head>
<meta charset="utf-8">
<title>DKA Business Card</title>
<link rel="stylesheet" href="https://fonts.googleapis.com/css2?family=Open+Sans:wght@400;600;700&family=Arimo:wght@400&display=swap">
<style>
  :root {
    --brand-blue: #0892d6;
    --brand-blue-deep: #0a7fc0;
    --paper: #ffffff;
    --ink: #2b2b2b;
    --ink-soft: #555555;
    --stage: #e9ebee;
  }
  * { box-sizing: border-box; margin: 0; padding: 0; }
  html, body {
    width: 1200px; height: 960px; overflow: hidden;
    background: var(--stage);
  }
  .card {
    position: absolute; left: 100px; top: 195px;
    width: 1000px; height: 571px;
    background: var(--paper);
    box-shadow: 0 10px 30px rgba(0,0,0,.18);
    overflow: hidden;
    font-family: "Open Sans", sans-serif;
  }
  .card-waves { position: absolute; inset: 0; width: 100%; height: 100%; }
  .wordmark {
    position: absolute; left: 50px; top: 52px;
    font-family: "Open Sans", sans-serif;
    font-weight: 700; font-size: 96px; line-height: 1;
    letter-spacing: 2px; color: var(--brand-blue);
  }
  .company-name {
    position: absolute; left: 52px; top: 172px;
    font-size: 19px; letter-spacing: .5px; text-transform: uppercase;
    color: var(--ink-soft);
  }
  .person { position: absolute; left: 52px; top: 226px; line-height: 1.35; }
  .person-name { font-weight: 700; font-size: 25px; color: var(--brand-blue-deep); }
  .person-role { font-size: 23px; color: var(--ink); }
  .contact {
    position: absolute; right: 44px; top: 146px;
    text-align: right; color: var(--paper);
    font-size: 22px; line-height: 32px;
  }
  .contact-line { display: flex; justify-content: flex-end; align-items: center; gap: 8px; }
  .contact-icon { width: 18px; height: 18px; fill: var(--paper); }
  .contact-address { margin-top: 8px; }
  .services {
    position: absolute; left: 48px; bottom: 34px;
    font-family: "Arimo", sans-serif; font-size: 23px;
    color: var(--paper); letter-spacing: .3px;
  }
</style>
</head>
<body>
  <section class="card">
    <svg class="card-waves" viewBox="0 0 1000 571" preserveAspectRatio="none" aria-hidden="true">
      <path fill="var(--brand-blue)" d="M1000,0 H735 C640,70 600,300 420,380 C300,430 150,430 0,400 V571 H1000 Z"/>
      <path fill="var(--paper)" d="M0,455 C250,472 470,420 595,262 C665,165 705,60 790,0 L815,0 C735,72 695,195 615,292 C485,452 245,492 0,476 Z"/>
      <path fill="none" stroke="var(--brand-blue)" stroke-width="3" d="M40,372 C200,402 370,392 470,350"/>
    </svg>

    <div class="wordmark">DKA</div>
    <div class="company-name">Dunmore Kesby &amp; Associates, Inc</div>

    <div class="person">
      <p class="person-name">Rosalind L. Kesby, CEO</p>
      <p class="person-role">Executive Coach</p>
      <p class="person-role">NVQ 4(c)</p>
    </div>

    <div class="contact">
      <p class="contact-line">020 481 3376
        <svg class="contact-icon" viewBox="0 0 24 24"><path d="M6.6 10.8a15 15 0 0 0 6.6 6.6l2.2-2.2c.3-.3.7-.4 1-.2 1.1.4 2.3.6 3.6.6.6 0 1 .4 1 1V20c0 .6-.4 1-1 1A17 17 0 0 1 3 4c0-.6.4-1 1-1h3.5c.6 0 1 .4 1 1 0 1.3.2 2.5.6 3.6.1.3 0 .7-.2 1z"/></svg>
      </p>
      <p class="contact-line">020 481 3377
        <svg class="contact-icon" viewBox="0 0 24 24"><path d="M7 2h9v5H7zM4 8h16a1 1 0 0 1 1 1v11a1 1 0 0 1-1 1H4a1 1 0 0 1-1-1V9a1 1 0 0 1 1-1zm3 4v2h4v-2zm0 4v2h4v-2zm7-4v2h3v-2zm0 4v2h3v-2z"/></svg>
      </p>
      <p class="contact-line">hello@dkacoach.com
        <svg class="contact-icon" viewBox="0 0 24 24"><path d="M2 5h20v14H2zm2 2v.5l8 5 8-5V7zm0 2.8V17h16V9.8l-8 5z"/></svg>
      </p>
      <p class="contact-line">www.dkacoach.com</p>
      <p class="contact-line contact-address">27.9th floor,Harlow Court</p>
      <p class="contact-line">Meridian Road LKG</p>
    </div>

    <p class="services">Coaching, Training, Diversity, Protocol</p>
  </section>
</body>
</html>
```